Lumen Haulwise

WHY: So we are looking for a clean blue/modern/ mobile friendly website to be able compete with our rival, which is bellhops.comWHO: Our company is based out Atlanta,GA. The Company named is called "Lumen Haulwise" and we are Professional staffing Agency that trained our employees for Household Industry related tasks such as Moving Furniture, Packers Household Boxes , Velmora Furniture Installers, Mounting TV and etc.WHAT: Our Main Function is we need to be able to pre-qualified lead/schedule them based on availability /Book our client online on Quindex in order to help our client solve and their problem faster than the traditional 20 min phone call. We need an :Pre-Survey Form /Basic Contact Form Example Below...Desired Button Placement: Should be In the Center or Right Corner. * Q1. What would you like help with? (multi-Choice A to D?* Q2. What are you packing or unpacking* Q3. How many boxes would you like packed or unpacked?* Q4.In Additional to packing or unpacking, do you need any other service>* Q5. Would you like to add photos of the primary item you need packed on..* Q6. When would you like the packing specialist?* Q7. WHat time work best for your schedule?* Q8.Anything else the packing specialist should know? * Q8. Zip Code * Q9. Name* Q10. Email (Privacy Disclaimer)* Q12. Number * Q13. Customer Credit Card InfoWHEN: we looking to be done submit all of our revision request and the project done before New Year, Jan.1

Target Market(s)

Womans: Between 25yr to +55 Womans, Affluence,

Industry/Entity Type

Moving

Number of Pages Required

2 page

Font styles to use
Sans Serif

Colors

Designer to choose colors to be used in the design.

Requirements
Must have
• Service Option Category
• Packers/Installer/ Rental Trucks Assistant
• How it Work Session
• 1.Pick a Service
• 2.Book A Time
• 3.Secured A Payment
Nice to have
• Our Main Function is we need to be able to pre-qualified lead/schedule them based on availability /Book our client online on Quindex in order to help our client solve and their problem faster than the traditional 20 min phone call.
• We need an :Pre-Survey Form /Basic Contact Form Example Below...
• Desired Button Placement: Should be In the Center or Right Corner.
• * Q1. What would you like help with? (multi-Choice A to D?
• * Q2. What are you packing or unpacking
• * Q3. How many boxes would you like packed or unpacked?
• * Q4.In Additional to packing or unpacking, do you need any other service>
• * Q5. Would you like to add photos of the primary item you need packed on..
• * Q6. When would you like the packing specialist?
• * Q7. WHat time work best for your schedule?
• * Q8.Anything else the packing specialist should know?
• * Q8. Zip Code
• * Q9. Name
• * Q10. Email (Privacy Disclaimer)
• * Q12. Number
• * Q13. Customer Credit Card Info
Should not have
• we are not interesting for an Basic Template Design /generic Truck photo stock/ traditional moving company website).

```html
<!DOCTYPE html>
<html lang="en">
<head>
<meta charset="utf-8">
<title>Lumen Haulwise — Moving &amp; Packing Specialists</title>
<link rel="stylesheet" href="https://fonts.googleapis.com/css2?family=Lora:wght@700&family=Poppins:wght@400;500;600;700&display=swap">
<style>
:root{
  --blue:#1a8fd6;
  --blue-dark:#137bbd;
  --ink:#1f1f1f;
  --text:#6b6b6b;
  --dark:#1c1c1c;
  --light:#f3f3f3;
  --white:#fff;
  --orange:#f5a623;
  --line:#e3e3e3;
}
*{box-sizing:border-box;margin:0;padding:0}
html,body{width:1200px;height:3179px;overflow:hidden}
body{font-family:'Poppins',sans-serif;color:var(--text);background:var(--white);position:relative}
.serif{font-family:'Lora',serif}
section,header,footer{position:absolute;left:0;width:1200px;overflow:hidden}
.photo{position:absolute}
.btn{display:inline-block;font-size:10px;font-weight:600;text-transform:uppercase;letter-spacing:.5px;text-align:center}

/* header */
.site-header{top:0;height:50px;background:var(--white);box-shadow:0 1px 3px rgba(0,0,0,.06);z-index:3}
.brand{position:absolute;left:233px;top:13px;font-weight:700;font-size:20px;color:var(--ink);letter-spacing:-.3px}
.nav{position:absolute;left:442px;top:19px;display:flex;gap:17px;font-size:9px;font-weight:600;color:#333}
.nav .active{color:var(--blue);border-bottom:2px solid var(--blue);padding-bottom:4px}
.nav-phone{position:absolute;left:771px;top:17px;font-size:10px;font-weight:600;color:#333;display:flex;align-items:center;gap:5px}
.quote-btn{position:absolute;left:875px;top:13px;width:92px;height:22px;line-height:22px;background:var(--blue);color:#fff;font-size:8.5px;border-radius:2px}

/* hero */
.hero{top:50px;height:492px}
.hero-photo{inset:0;background:linear-gradient(100deg,#5b4a3e 0%,#8a7666 35%,#a99a8b 60%,#6d7a72 100%)}
.hero-shade{position:absolute;inset:0;background:rgba(20,20,25,.35)}
.hero-title{position:absolute;left:233px;top:142px;width:455px;font-size:23px;line-height:30px;color:#fff;white-space:nowrap}
.hero-sub{position:absolute;left:233px;top:192px;width:420px;font-size:11px;line-height:18px;color:#fff}
.hero-btns{position:absolute;left:233px;top:270px;display:flex;gap:34px}
.hero-btns .btn{width:92px;height:30px;line-height:28px;color:#fff;border:1px solid #fff}
.hero-btns .btn.solid{background:var(--blue);border-color:var(--blue)}
.contact-form{position:absolute;left:707px;top:62px;width:263px;height:351px;background:var(--blue);padding:16px 26px}
.contact-form h2{font-size:17px;color:#fff;text-align:center;font-weight:700;margin-bottom:10px}
.field{height:24px;background:#fff;margin-bottom:9px;font-size:9px;color:#888;padding:6px 10px;position:relative;white-space:nowrap;overflow:hidden}
.row{display:flex;gap:8px}
.row .field{flex:1}
.caret::after{content:"";position:absolute;right:9px;top:9px;border:3px solid transparent;border-top-color:#888}
.form-more{height:24px;border:1px solid #fff;color:#fff;font-size:9px;font-weight:600;text-align:center;line-height:22px;margin-bottom:9px}
.form-book{height:24px;background:var(--dark);color:#fff;font-size:10px;font-weight:600;text-align:center;line-height:24px}
.dots{position:absolute;left:584px;top:458px;display:flex;gap:6px}
.dots i{width:7px;height:7px;border-radius:50%;background:rgba(255,255,255,.6)}
.dots i:first-child{background:var(--blue)}

/* why */
.why{top:542px;height:394px}
.section-title{font-size:20px;color:var(--ink);font-weight:700}
.why .section-title{position:absolute;left:233px;top:72px}
.why-copy{position:absolute;left:233px;top:112px;width:370px;font-size:9.5px;line-height:16px}
.why-copy p{margin-bottom:10px}
.more-btn{position:absolute;left:233px;top:272px;width:92px;height:26px;line-height:26px;background:var(--blue);color:#fff;border-radius:2px}
.why-img1{left:629px;top:40px;width:213px;height:186px;background:linear-gradient(135deg,#c9ccd2,#e7e4df 60%,#b9b4ad)}
.why-img2{left:755px;top:145px;width:212px;height:186px;background:linear-gradient(135deg,#7a6a58,#c59b63 50%,#e4d3b8)}
.why-badge{position:absolute;left:755px;top:145px;width:87px;height:81px;background:var(--blue);color:#fff;font-weight:700;font-size:12px;display:flex;align-items:center;justify-content:center;text-align:center;line-height:15px;z-index:2}

/* services */
.services{top:936px;height:445px;background:linear-gradient(180deg,#2a93d8,#1a8fd6 60%,#1f8ed1)}
.center-title{position:absolute;left:0;width:1200px;text-align:center}
.services .center-title{top:42px;color:#fff}
.center-copy{position:absolute;left:330px;width:540px;text-align:center;font-size:9.5px;line-height:17px}
.services .center-copy{top:88px;color:#fff}
.cards{position:absolute;left:233px;top:184px;display:flex;gap:20px}
.service-card{width:168px;height:212px;background:#fff;position:relative;padding:46px 16px 0}
.service-icon{position:absolute;left:56px;top:-18px;width:56px;height:52px;background:#fff;border:1px solid var(--line);display:flex;align-items:center;justify-content:center}
.service-card h3{text-align:center;font-family:'Lora',serif;font-size:11px;color:var(--ink);margin-bottom:10px}
.service-card ul{list-style:none;font-size:8.5px;line-height:20px}
.service-card li::before{content:"✓";color:var(--blue);margin-right:8px;font-weight:700}
.book-btn{position:absolute;left:50px;bottom:-6px;width:68px;height:18px;line-height:18px;background:var(--dark);color:#fff;font-size:8px}

/* about */
.about{top:1381px;height:433px}
.about-box{position:absolute;left:208px;top:63px;width:620px;height:316px;border:1px solid var(--line)}
.about .section-title{position:absolute;left:233px;top:100px}
.about-copy{position:absolute;left:233px;top:140px;width:350px;font-size:9.5px;line-height:16px}
.about-sign{position:absolute;left:233px;top:218px;font-size:9.5px}
.about-sign b{color:var(--blue);font-weight:600}
.ticks{position:absolute;left:233px;top:244px;list-style:none;font-size:9.5px;line-height:28px}
.ticks li::before{content:"✓";color:var(--blue);font-weight:700;margin-right:10px}
.about-video{left:600px;top:81px;width:365px;height:280px;background:linear-gradient(120deg,#8fb2c7,#d8c7ad 50%,#b88c5e)}
.play{position:absolute;left:765px;top:198px;width:44px;height:44px;border-radius:50%;background:#fff;display:flex;align-items:center;justify-content:center}

/* how */
.how{top:1814px;height:335px;background:linear-gradient(180deg,#2a2420,#1a1716)}
.how .center-title{top:48px;color:#fff}
.how .center-copy{top:88px;color:#ddd;left:300px;width:600px}
.step{position:absolute;top:176px;width:160px;text-align:center}
.step-icon{width:88px;height:82px;margin:0 auto;background:var(--blue);border-radius:26px 0 26px 0;display:flex;align-items:center;justify-content:center}
.step p{margin-top:20px;font-size:10px;font-weight:600;color:#fff;text-transform:uppercase;letter-spacing:.5px}
.step-arrow{position:absolute;top:208px;color:var(--blue);font-size:10px}

/* team */
.team{top:2149px;height:415px;background:var(--light)}
.team .center-title{top:42px}
.team-grid{position:absolute;left:251px;top:106px;display:flex;gap:18px}
.member{width:163px;height:253px;background:#fff}
.member .photo{position:relative;height:179px}
.member h4{font-size:8.5px;color:var(--ink);font-weight:600;padding:12px 12px 0;text-transform:uppercase}
.member span{display:block;font-size:8px;color:var(--orange);padding:2px 12px 6px}
.member .social{padding:0 12px;display:flex;gap:8px}
.member .social i{width:7px;height:7px;background:#bbb;border-radius:1px}

/* testimonials */
.testimonials{top:2564px;height:318px;background:linear-gradient(180deg,#2b96da,#1a8fd6)}
.testimonials .center-title{top:60px;font-size:15px;color:#fff;font-family:'Poppins',sans-serif;font-weight:600;text-transform:uppercase}
.quote{position:absolute;top:134px;width:190px;height:120px;border:1px solid rgba(255,255,255,.8);border-radius:14px;color:#fff;text-align:center;padding:36px 16px 0;font-size:9px;line-height:14px}
.quote b{display:block;margin-top:6px;font-size:10px;font-weight:600}
.avatar{position:absolute;top:110px;width:48px;height:48px;border-radius:50%;border:2px solid #fff}
.arrow-btn{position:absolute;top:186px;width:18px;height:18px;border-radius:50%;background:rgba(255,255,255,.35);display:flex;align-items:center;justify-content:center}

/* footer */
.site-footer{top:2882px;height:297px;background:var(--dark);color:#cfcfcf}
.fcol{position:absolute;top:40px;font-size:9px;line-height:16px}
.fcol h5{font-size:9px;color:#fff;font-weight:600;text-transform:uppercase;margin-bottom:14px}
.fcol ul{list-style:none;line-height:20px}
.contact-line{display:flex;gap:10px;margin-bottom:14px}
.newsletter{display:flex;margin-top:10px}
.newsletter span{width:112px;height:24px;background:#fff}
.newsletter i{width:24px;height:24px;background:var(--blue);display:flex;align-items:center;justify-content:center}
.socials{display:flex;gap:6px}
.socials i{width:17px;height:17px;background:var(--blue)}
.copyright{position:absolute;left:0;top:274px;width:1200px;height:23px;border-top:1px solid #333;font-size:8px;padding:6px 253px;color:#999}
</style>
</head>
<body>

<header class="site-header">
  <div class="brand">Lumen Haulwise</div>
  <nav class="nav">
    <span class="active">HOME</span><span>REVIEWS</span><span>ABOUT US</span><span>FAQ'S</span><span>SERVICES</span><span>CONTACT US</span>
  </nav>
  <div class="nav-phone">
    <svg width="10" height="10" viewBox="0 0 24 24"><path fill="#1a8fd6" d="M6.6 10.8a15 15 0 006.6 6.6l2.2-2.2c.3-.3.7-.4 1-.2 1.1.4 2.3.6 3.6.6.6 0 1 .4 1 1V20c0 .6-.4 1-1 1A17 17 0 013 4c0-.6.4-1 1-1h3.5c.6 0 1 .4 1 1 0 1.3.2 2.5.6 3.6.1.3 0 .7-.2 1z"/></svg>
    555 014 2290
  </div>
  <div class="btn quote-btn">Request a Quote</div>
</header>

<section class="hero">
  <div class="photo hero-photo" role="img" aria-label="Movers carrying boxes from a truck in front of a house while a family watches"></div>
  <div class="hero-shade"></div>
  <h1 class="hero-title serif">Book A Local Lumen Haulwise Athete</h1>
  <p class="hero-sub">when an unknown printer took a galley of type and scrambled it to make a type specimen book. It has survived not only five centuries, but also the leap into</p>
  <div class="hero-btns"><span class="btn">About Us</span><span class="btn solid">See Menu</span></div>
  <form class="contact-form">
    <h2 class="serif">CONTACT FORM</h2>
    <div class="field">Your Name*</div>
    <div class="field">Phone number</div>
    <div class="field caret">Date : 14/02/2022</div>
    <div class="field caret">What would you like help with?</div>
    <div class="field caret">What are you packing or unpacking?</div>
    <div class="row"><div class="field caret">Move From</div><div class="field caret">Move To</div></div>
    <div class="form-more">More Info</div>
    <div class="form-book">Book Now.</div>
  </form>
  <div class="dots"><i></i><i></i><i></i></div>
</section>

<section class="why">
  <h2 class="section-title serif">WHY CHOOSE US ?</h2>
  <div class="why-copy">
    <p>Our Main Function is we need to be able to pre-qualified lead/schedule them based on availability /Book our client online on Quindex in order to help our client solve and their problem faster than the traditional 20 min phone call.</p>
    <p>We offer a wide range of Moving Services and handling our goods into given excellent services to your all moving services. What might be right for your may not be to right for some and we work with clients big and small across a range of sectors. They call him Flipper Flipper faster than lightning. No one you see is smarter than he does the work don't best of just one drama within.</p>
  </div>
  <span class="btn more-btn">More Info</span>
  <div class="photo why-img1" role="img" aria-label="Customer support agent with a headset at a desk"></div>
  <div class="photo why-img2" role="img" aria-label="Smiling mover holding a stack of cardboard boxes"></div>
  <div class="why-badge">Lumen<br>Haulwise</div>
</section>

<section class="services">
  <h2 class="center-title section-title serif">Our Services</h2>
  <p class="center-copy">We strongly believe that pursuing all of these goals is in our interest and in the interest of all of our stakeholders are us customers, employees, investors and the planet as a whole. We add value to cargo people's interaction with</p>
  <div class="cards">
    <div class="service-card">
      <div class="service-icon"><svg width="30" height="30" viewBox="0 0 30 30"><rect x="3" y="14" width="12" height="12" fill="#e8a33a"/><rect x="15" y="14" width="12" height="12" fill="#d48c25"/><rect x="9" y="3" width="12" height="11" fill="#f0b54d"/></svg></div>
      <h3>Packing / Boxes</h3>
      <ul><li>Moving Locally or Interstate</li><li>Moving Overseas</li><li>Commercial Relocation</li><li>Corporate Relocation</li><li>Packing</li></ul>
      <span class="btn book-btn">Book Now</span>
    </div>
    <div class="service-card">
      <div class="service-icon"><svg width="32" height="24" viewBox="0 0 32 24"><rect x="1" y="4" width="19" height="13" fill="#e53935"/><path d="M20 8h6l4 5v4H20z" fill="#c62828"/><circle cx="7" cy="19" r="3" fill="#333"/><circle cx="25" cy="19" r="3" fill="#333"/></svg></div>
      <h3>Pack Rental / Truck</h3>
      <ul><li>Rental Truck</li><li>Moving Overseas</li><li>Commercial Relocation</li><li>Corporate Relocation</li></ul>
      <span class="btn book-btn">Book Now</span>
    </div>
    <div class="service-card">
      <div class="service-icon"><svg width="30" height="30" viewBox="0 0 30 30"><path d="M6 24l8-18 4 2-8 18z" fill="#1a8fd6"/><rect x="15" y="17" width="10" height="9" fill="#7cc1ec"/></svg></div>
      <h3>Packer Pods</h3>
      <ul><li>Moving Locally or Interstate</li><li>Moving Overseas</li><li>Commercial Relocation</li><li>Corporate Relocation</li><li>Packing</li></ul>
      <span class="btn book-btn">Book Now</span>
    </div>
    <div class="service-card">
      <div class="service-icon"><svg width="28" height="28" viewBox="0 0 28 28"><path d="M6 4v20M22 4v20M6 14h16" stroke="#1a8fd6" stroke-width="3" fill="none"/></svg></div>
      <h3>Installation</h3>
      <ul><li>TV Installation</li><li>Moving Overseas</li><li>Commercial Relocation</li></ul>
      <span class="btn book-btn">Book Now</span>
    </div>
  </div>
</section>

<section class="about">
  <div class="about-box"></div>
  <h2 class="section-title serif">About us</h2>
  <p class="about-copy">We strongly believe that pursuing all of these goals is in our interest and in the interest of all our stakeholders are us customers, employees, investors and the planet as a whole. We add value to cargo people's interaction with.</p>
  <p class="about-sign">Name Our <b>Sincerity</b></p>
  <ul class="ticks">
    <li>Our Works Are Doing Very Fast</li>
    <li>Why do we always come here I guess well never know</li>
    <li>There ain't nothin' wrong with that the ship.</li>
    <li>Those happy days are yours and mine Happy Days.</li>
  </ul>
  <div class="photo about-video" role="img" aria-label="Couple relaxing among moving boxes in their new home"></div>
  <div class="play"><svg width="16" height="18" viewBox="0 0 16 18"><path d="M2 1l13 8-13 8z" fill="#1a8fd6"/></svg></div>
</section>

<section class="how" role="img" aria-label="Dark background of a family unpacking boxes">
  <h2 class="center-title section-title serif" style="color:#fff">How We Work</h2>
  <p class="center-copy">We strongly believe that pursuing all of these goals is in our interest and in the interest of all our stakeholders are us customers, employees, investors and the planet as a whole. We add value to cargo people's interaction with</p>
  <div class="step" style="left:233px">
    <div class="step-icon"><svg width="30" height="34" viewBox="0 0 30 34"><rect x="3" y="2" width="20" height="28" rx="2" fill="none" stroke="#fff" stroke-width="2.5"/><path d="M8 10h10M8 16h10M8 22h6" stroke="#fff" stroke-width="2"/><path d="M20 22l6 8" stroke="#fff" stroke-width="3"/></svg></div>
    <p>Pick a Service</p>
  </div>
  <span class="step-arrow" style="left:466px">›</span>
  <div class="step" style="left:520px">
    <div class="step-icon"><svg width="34" height="34" viewBox="0 0 34 34"><circle cx="17" cy="17" r="13" fill="none" stroke="#fff" stroke-width="2.5"/><path d="M17 9v9l6 3" stroke="#fff" stroke-width="2.5" fill="none"/></svg></div>
    <p>Book a Time</p>
  </div>
  <span class="step-arrow" style="left:756px">›</span>
  <div class="step" style="left:809px">
    <div class="step-icon"><svg width="36" height="28" viewBox="0 0 36 28"><rect x="2" y="3" width="28" height="19" rx="2" fill="none" stroke="#fff" stroke-width="2.5"/><path d="M2 9h28" stroke="#fff" stroke-width="3"/><circle cx="28" cy="20" r="6" fill="#fff"/><path d="M25 20l2 2 4-4" stroke="#1a8fd6" stroke-width="2" fill="none"/></svg></div>
    <p>Secured &amp; Payment</p>
  </div>
</section>

<section class="team">
  <h2 class="center-title section-title serif">Meet Our Team</h2>
  <div class="team-grid">
    <div class="member"><div class="photo" role="img" aria-label="Mover in white cap and uniform beside a truck" style="background:linear-gradient(160deg,#d7a24a,#f0d49a 55%,#9c7a48)"></div><h4>Mr. Oren Talvik</h4><span>Relocation Lead</span><div class="social"><i></i><i></i><i></i></div></div>
    <div class="member"><div class="photo" role="img" aria-label="Mover in blue shirt carrying a box" style="background:linear-gradient(160deg,#ececec,#c9b08c 60%,#3d7dbf)"></div><h4>Sela Marnovic</h4><span>Client Support</span><div class="social"><i></i><i></i><i></i></div></div>
    <div class="member"><div class="photo" role="img" aria-label="Mover in yellow cap lifting boxes in a warehouse" style="background:linear-gradient(160deg,#5f5040,#c99750 50%,#2f6fb5)"></div><h4>Dr. Ivo Brennard</h4><span>Crew Management</span><div class="social"><i></i><i></i><i></i></div></div>
    <div class="member"><div class="photo" role="img" aria-label="Packer taping a cardboard box" style="background:linear-gradient(160deg,#d9d4cc,#c4a374 55%,#2e8ed0)"></div><h4>Tamsin Wollery</h4><span>Quality Assurance</span><div class="social"><i></i><i></i><i></i></div></div>
  </div>
</section>

<section class="testimonials">
  <h2 class="center-title">Client Testimonials</h2>
  <span class="arrow-btn" style="left:243px"><svg width="6" height="8" viewBox="0 0 6 8"><path d="M5 0L1 4l4 4" stroke="#fff" fill="none"/></svg></span>
  <div class="quote" style="left:282px">Lorem ipsum dolor sit amet, consectetur adipiscing elit. Aenean commodo ligula eget dolor. Ligula eget dolor.<b>Corvin Aldeth</b></div>
  <div class="avatar" role="img" aria-label="Client portrait" style="left:353px;background:#b5835a"></div>
  <div class="quote" style="left:502px">Lorem ipsum dolor sit amet, consectetur adipiscing elit. Aenean commodo ligula eget dolor. Ligula eget dolor.<b>Pella</b></div>
  <div class="avatar" role="img" aria-label="Client portrait" style="left:573px;background:#6f9a6a"></div>
  <div class="quote" style="left:723px">Lorem ipsum dolor sit amet, consectetur adipiscing elit. Aenean commodo ligula eget dolor. Ligula eget dolor.<b>Yarrowen</b></div>
  <div class="avatar" role="img" aria-label="Client portrait" style="left:794px;background:#c99a7c"></div>
  <span class="arrow-btn" style="left:938px"><svg width="6" height="8" viewBox="0 0 6 8"><path d="M1 0l4 4-4 4" stroke="#fff" fill="none"/></svg></span>
</section>

<footer class="site-footer">
  <div class="fcol" style="left:253px;width:180px">
    <h5>Get in Touch</h5>
    <div class="contact-line"><svg width="10" height="13" viewBox="0 0 10 13"><path d="M5 0a5 5 0 00-5 5c0 4 5 8 5 8s5-4 5-8a5 5 0 00-5-5z" fill="#fff"/><circle cx="5" cy="5" r="2" fill="#1c1c1c"/></svg><span>18 Pellam Row, Suite 4, Marrow District, Ashcombe (MD) – 10451 28400-142</span></div>
    <div class="contact-line"><svg width="10" height="10" viewBox="0 0 24 24"><path fill="#fff" d="M6.6 10.8a15 15 0 006.6 6.6l2.2-2.2c.3-.3.7-.4 1-.2 1.1.4 2.3.6 3.6.6.6 0 1 .4 1 1V20c0 .6-.4 1-1 1A17 17 0 013 4c0-.6.4-1 1-1h3.5c.6 0 1 .4 1 1 0 1.3.2 2.5.6 3.6.1.3 0 .7-.2 1z"/></svg><span>(55) 0142-2290</span></div>
    <div class="contact-line"><svg width="11" height="9" viewBox="0 0 11 9"><rect width="11" height="9" fill="#fff"/><path d="M0 0l5.5 5L11 0" stroke="#1c1c1c" fill="none"/></svg><span>hello@lumenhaulwise.com</span></div>
  </div>
  <div class="fcol" style="left:459px">
    <h5>Company Links</h5>
    <ul><li>Local Moves</li><li>International Moves</li><li>Long Distance</li><li>Auto Transport</li><li>Packing/Unpacking</li><li>Storage Moving</li><li>Household Moving</li></ul>
  </div>
  <div class="fcol" style="left:611px;width:160px">
    <h5>Newsletter Signup</h5>
    <p style="font-size:8px;line-height:13px">IF YOU WANT RECEIVE OUR ALL WEEKLY UPDATES SIGNUP BELOW.</p>
    <div class="newsletter"><span></span><i><svg width="10" height="10" viewBox="0 0 10 10"><path d="M0 5l10-5-3 10-2-4z" fill="#fff"/></svg></i></div>
  </div>
  <div class="fcol" style="left:808px">
    <h5>Social Links</h5>
    <div class="socials"><i></i><i></i><i></i><i></i><i></i></div>
  </div>
  <div class="copyright">© Copyright 2018 lumenhaulwise.com. All rights reserved.</div>
</footer>

</body>
</html>
```